Letterhead

We would like to use the logo attached as a new letterhead. Our problem is that we think the dark blue background is too much. We'd like a sleek, professional letterhead, and we'd like at least five options to choose from. I've also uploaded our old letterhead for reference of the style we're going for.

```html
<!DOCTYPE html>
<html lang="en">
<head>
<meta charset="utf-8">
<title>Harbor Line Partners Letterhead</title>
<link rel="stylesheet" href="https://fonts.googleapis.com/css2?family=Tinos:wght@400;700&family=Cinzel:wght@500&family=Dancing+Script:wght@500&display=swap">
<style>
  :root {
    --navy: #1c2f4d;
    --gold: #c9a55f;
    --paper: #ffffff;
    --ink: #111111;
    --backdrop: #e4e4e4;
    --faint: #e8e9ec;
  }
  * { margin: 0; padding: 0; box-sizing: border-box; }
  html, body { width: 1200px; height: 1200px; overflow: hidden; }
  body { background: var(--backdrop); font-family: "Tinos", "Times New Roman", serif; }
  .letterhead {
    position: absolute; left: 191px; top: 22px;
    width: 818px; height: 1158px;
    background: var(--navy); overflow: hidden;
  }
  .letterhead-frame { position: absolute; inset: 0; width: 818px; height: 1158px; }
  .brand {
    position: absolute; left: 88px; top: 100px;
    display: flex; align-items: center; gap: 16px;
  }
  .brand-mark { width: 22px; height: 22px; background: var(--gold); }
  .brand-name {
    font-family: "Tinos", "Times New Roman", serif; font-weight: 700;
    font-size: 40px; letter-spacing: 1px; color: var(--navy);
    text-transform: uppercase;
  }
  .letter-date {
    position: absolute; right: 85px; top: 278px;
    font-size: 17px; color: var(--ink);
  }
  .letter-body {
    position: absolute; left: 88px; top: 307px; width: 700px;
    font-size: 17px; line-height: 36.6px; color: var(--ink);
    white-space: nowrap;
  }
  .letter-body p { margin-bottom: 36.6px; }
  .letter-body .letter-closing { margin-bottom: 0; }
  .signature {
    font-family: "Dancing Script", cursive; font-size: 28px;
    line-height: 1; margin-top: 4px;
  }
  .footer-contact {
    position: absolute; left: 0; right: 0; top: 1087px;
    text-align: center; font-family: "Cinzel", "Times New Roman", serif;
    font-size: 11.5px; letter-spacing: 1px; color: #ffffff;
  }
</style>
</head>
<body>
  <main class="letterhead">
    <svg class="letterhead-frame" viewBox="0 0 818 1158" aria-hidden="true">
      <path class="paper-sheet" d="M0,143 C60,65 150,25 300,25 L818,25 L818,958 C760,1040 680,1075 560,1075 L0,1075 Z" fill="var(--paper)"/>
      <rect class="watermark-square" x="540" y="858" width="195" height="200" fill="var(--faint)"/>
      <path class="footer-band" d="M818,958 C760,1040 680,1075 560,1075 L0,1075 L0,1158 L818,1158 Z" fill="var(--navy)"/>
      <path class="gold-rule-top" d="M0,143 C60,65 150,25 300,25 L818,25" fill="none" stroke="var(--gold)" stroke-width="3.5"/>
      <path class="gold-rule-bottom" d="M818,958 C760,1040 680,1075 560,1075 L0,1075" fill="none" stroke="var(--gold)" stroke-width="3.5"/>
    </svg>

    <div class="brand">
      <span class="brand-mark"></span>
      <span class="brand-name">Harbor Line Partners</span>
    </div>

    <div class="letter-date">December 21, 2025</div>

    <div class="letter-body">
      <p>Dear Sir,</p>
      <p>Thank you for inviting me to design your new letterhead.</p>
      <p>This letterhead is designed to embody simplicity, professionalism, and brand consistency.<br>
      By using a clean layout with generous white space, the design ensures readability and<br>
      a modern, uncluttered look. Your logo is placed prominently but tastefully, reinforcing brand<br>
      recognition without overpowering the content. The color palette is based on navy blue and<br>
      gold, maintaining a strong visual connection to the brand’s identity. Professional serif<br>
      typography complements the contemporary style, ensuring that official correspondence looks<br>
      polished and credible.</p>
      <p>Overall, the design balances corporate sophistication with the energetic, youthful spirit that<br>
      defines your firm. I hope you like it.</p>
      <p class="letter-closing">Best Regards,</p>
      <div class="signature">Clara</div>
    </div>

    <div class="footer-contact">318 Cedar Row · Suite 210 · Portland, Maine 04101 · 207 555 0148 · hello@harborlinepartners.com</div>
  </main>
</body>
</html>
```